Medical group practice

We need a flyer design incorporating the three doctors in the practice, there is a general practitioner, ophthalmologist and an obstetrician & Gynaecologist. see the attached file for the concept. will leave the colour design up to you

Target Market(s)

general public

Industry/Entity Type

Health Care

Colors

Designer to choose colors to be used in the design.

Requirements
Must have
• logos included in attachement

```html
<!DOCTYPE html>
<html lang="en">
<head>
<meta charset="utf-8">
<title>Brightwell Medical Flyer</title>
<link href="https://fonts.googleapis.com/css2?family=Exo+2:wght@400;500;600;700&display=swap" rel="stylesheet">
<style>
  :root{
    --backdrop:#c3c3cc;
    --red-deep:#be2a24;
    --red-mid:#c62c25;
    --red-warm:#c4372c;
    --body-1:#c74433;
    --body-2:#cb4f3a;
    --body-3:#d66c4f;
    --foot-1:#6a2523;
    --foot-2:#7a2a26;
    --foot-3:#86302b;
    --band:#d3241f;
    --band-soft:rgba(214,52,44,.72);
    --logo-grey:#6b6b72;
    --white:#ffffff;
  }
  *{margin:0;padding:0;box-sizing:border-box}
  html,body{width:1200px;height:1200px;overflow:hidden}
  body{background:var(--backdrop);font-family:"Exo 2",Arial,sans-serif;color:var(--white);position:relative}

  .flyer{position:absolute;left:269px;top:107px;width:688px;height:976px;background:var(--white);
    box-shadow:0 2px 8px rgba(0,0,0,.18);overflow:hidden}

  .hero{position:relative;height:322px}
  .hero-photo{position:absolute;inset:0;
    background:linear-gradient(100deg,#f3f3f5 0%,#e6e7ea 30%,#d9dcdf 45%,#eef1f2 60%,#d5e6ea 80%,#f6f7f8 100%)}
  .brand{position:absolute;left:386px;top:36px;display:flex;align-items:center;gap:14px}
  .brand-dot{width:40px;height:40px;border-radius:50%;background:var(--red-mid)}
  .brand-name{color:var(--logo-grey);font-weight:600;font-size:30px;line-height:1.1}
  .band{position:absolute;left:0;right:0}
  .band-top{top:150px;height:28px;background:var(--band-soft)}
  .band-main{top:178px;height:40px;background:var(--band)}
  .band-low{top:218px;height:24px;background:var(--band-soft)}
  .tagline{position:absolute;left:0;right:0;top:172px;text-align:center;font-size:38px;font-weight:500;letter-spacing:.2px}

  .grid{display:grid;grid-template-columns:229px 230px 229px;grid-template-rows:100px 116px 304px 134px}
  .cell{text-align:center;font-size:15px;line-height:1.38}
  .c1{background:var(--red-deep)} .c2{background:var(--red-mid)} .c3{background:var(--red-warm)}
  .b1{background:var(--body-1)} .b2{background:var(--body-2)} .b3{background:var(--body-3)}
  .f1{background:var(--foot-1)} .f2{background:var(--foot-2)} .f3{background:var(--foot-3)}

  .icon-cell{display:flex;align-items:center;justify-content:center}
  .icon-slot{width:64px;height:56px;border-radius:8px;background:rgba(255,255,255,.28)}
  .head-cell{padding-top:14px}
  .specialty{font-weight:700}
  .body-cell{padding-top:12px}
  .doctor{font-weight:700;min-height:90px}
  .services{list-style:none;text-align:left;padding-left:50px;font-size:14.5px;line-height:1.38;margin-top:20px}
  .b2 .services{padding-left:34px}
  .b3 .services{padding-left:22px}
  .foot-cell{display:flex;flex-direction:column;justify-content:center;align-items:center}
  .foot-label{font-weight:700;font-size:15.5px}
  .hours strong{font-weight:700;display:block}
</style>
</head>
<body>
  <main class="flyer">
    <header class="hero">
      <div class="hero-photo" role="img" aria-label="Photo of a doctor in a white coat holding a stethoscope in a bright clinic"></div>
      <div class="brand">
        <span class="brand-dot"></span>
        <span class="brand-name">Brightwell<br>Medical</span>
      </div>
      <div class="band band-top"></div>
      <div class="band band-main"></div>
      <div class="band band-low"></div>
      <h1 class="tagline">Your Health is Our Priority</h1>
    </header>

    <section class="grid">
      <div class="cell c1 icon-cell"><div class="icon-slot" role="img" aria-label="General practice icon"></div></div>
      <div class="cell c2 icon-cell"><div class="icon-slot" role="img" aria-label="Eye care icon"></div></div>
      <div class="cell c3 icon-cell"><div class="icon-slot" role="img" aria-label="Mother and child icon"></div></div>

      <div class="cell c1 head-cell"><div class="specialty">GENERAL<br>PRACTITIONER</div>(869) 555 0139,</div>
      <div class="cell c2 head-cell"><div class="specialty"><br>OPHTHALMOLOGIST</div>(869) 555 0124,</div>
      <div class="cell c3 head-cell"><div class="specialty">OBSTETRICIAN/<br>GYNAECOLOGIST</div>(869 ) 555 0150<br>(869) 555 0161</div>

      <div class="cell b1 body-cell">
        <div class="doctor">DR. MARCUS<br>ELWOOD, MD.</div>
        <ul class="services">
          <li>General Checks</li><li>Annual Check ups</li><li>Wound Care/Dressings</li><li>Incision &amp; Drainage</li>
          <li>Suturing lacerations</li><li>Pain Injections</li><li>Glucose checks</li><li>Foreign Body Removal</li>
        </ul>
      </div>
      <div class="cell b2 body-cell">
        <div class="doctor">DR. LUCIA R.<br>FONTAINE MD.<br>ClearSight<br>Vision Services</div>
        <ul class="services">
          <li>Eyes disease</li><li>examination,</li><li>Surgery of Pterygium,</li><li>Cataract, Glaucoma,</li>
          <li>Emergency:</li><li>Conjunctivitis,</li><li>Traumatism,</li><li>Foreign body and more</li>
        </ul>
      </div>
      <div class="cell b3 body-cell">
        <div class="doctor">DR. VIKRAM DESAI,<br>BMedSci, MBBS,<br>DM (O&amp;G), FACOG</div>
        <ul class="services">
          <li>Obstetrics: Prenatal Care,</li><li>Delivery, Postnatal checks,</li><li>High Risk pregnancy</li>
          <li>Gynaecology: Pap smears,</li><li>Abnormal vaginal bleeding,</li><li>Fibroids, Colposcopy,</li>
          <li>Family planning,</li><li>Infertility,Cancer screening,</li><li>And More….</li>
        </ul>
      </div>

      <div class="cell f1 foot-cell"><span class="foot-label">OPENING HOURS</span></div>
      <div class="cell f2 foot-cell hours"><strong>MONDAY-FRIDAY</strong>9am – 6pm<strong>SATURDAYS</strong>10am – 5pm</div>
      <div class="cell f3 foot-cell">42 Harbour Lane,<br>Basseterre, St. Kitts<br>Tel : (869) 555 0172 / 0173</div>
    </section>
  </main>
</body>
</html>
```